Velt Harbor Solutions

I have a file with a logo. It is grainy. I also have a board with my color pallet and other branding items. I need a file with the logo that is high resolution and I also need a business card design.

```html
<!DOCTYPE html>
<html lang="en">
<head>
<meta charset="utf-8">
<title>Velt Harbor Solutions — Business Card</title>
<link href="https://fonts.googleapis.com/css2?family=Montserrat:wght@400;500;700;800&display=swap" rel="stylesheet">
<style>
  :root {
    --backdrop: #4a4a4c;
    --card-white: #ffffff;
    --navy: #232b38;
    --slate: #4d6079;
    --brand-red: #9b1b22;
    --ink: #1f2530;
  }
  * { box-sizing: border-box; margin: 0; padding: 0; }
  html, body {
    width: 1200px; height: 1200px; overflow: hidden;
    background: var(--backdrop);
    font-family: "Montserrat", Arial, sans-serif;
  }
  .sheet {
    position: relative; width: 1200px; height: 1200px;
    display: flex; flex-direction: column; align-items: center; justify-content: center; gap: 70px;
  }
  .card {
    position: relative; width: 760px; height: 434px;
    border-radius: 34px; overflow: hidden;
    box-shadow: 0 18px 40px rgba(0,0,0,0.35);
  }
  .card-front { background: var(--card-white); }
  .card-back { background: var(--navy); display: flex; align-items: center; justify-content: center; }

  .front-bands { position: absolute; left: 0; bottom: 0; width: 760px; height: 40px; }

  .identity { position: absolute; left: 52px; top: 118px; }
  .person-name {
    color: var(--brand-red); font-weight: 800; font-size: 42px; letter-spacing: 0.5px; line-height: 1;
  }
  .person-title {
    color: var(--ink); font-weight: 500; font-size: 28px; margin-top: 10px; line-height: 1;
  }
  .contact-list { list-style: none; margin-top: 22px; }
  .contact-list li {
    display: flex; align-items: center; gap: 16px;
    color: var(--ink); font-size: 24px; font-weight: 400; line-height: 1; margin-bottom: 14px;
  }
  .contact-list svg { width: 26px; height: 26px; flex: none; }

  .brand-lockup {
    position: absolute; right: 56px; top: 118px;
    display: flex; align-items: center; gap: 18px;
  }
  .brand-square { width: 54px; height: 54px; background: var(--brand-red); flex: none; }
  .brand-name {
    font-weight: 800; font-size: 38px; line-height: 1.05; letter-spacing: 1px;
    color: var(--navy); text-transform: uppercase;
  }
  .brand-name-back { color: var(--card-white); text-align: center; }
</style>
</head>
<body>
<main class="sheet">
  <section class="card card-front" aria-label="Business card front">
    <div class="identity">
      <p class="person-name">FULL NAME</p>
      <p class="person-title">TITLE</p>
      <ul class="contact-list">
        <li>
          <svg viewBox="0 0 24 24" aria-hidden="true"><path fill="#9b1b22" d="M6.6 10.8a15 15 0 0 0 6.6 6.6l2.2-2.2c.3-.3.7-.4 1-.2 1.1.4 2.3.6 3.6.6.6 0 1 .4 1 1V20c0 .6-.4 1-1 1A17 17 0 0 1 3 4c0-.6.4-1 1-1h3.5c.6 0 1 .4 1 1 0 1.3.2 2.5.6 3.6.1.3 0 .7-.2 1z"/></svg>
          (000) 000 0000
        </li>
        <li>
          <svg viewBox="0 0 24 24" aria-hidden="true"><rect x="2" y="5" width="20" height="14" fill="#9b1b22"/><path d="M2 5l10 8 10-8" fill="none" stroke="#fff" stroke-width="1.6"/></svg>
          email@company.com
        </li>
        <li>
          <svg viewBox="0 0 24 24" aria-hidden="true"><g fill="none" stroke="#9b1b22" stroke-width="1.8"><circle cx="12" cy="12" r="9.5"/><ellipse cx="12" cy="12" rx="4.2" ry="9.5"/><path d="M2.5 12h19M4 7h16M4 17h16"/></g></svg>
          www.company.com
        </li>
      </ul>
    </div>

    <div class="brand-lockup">
      <span class="brand-square" aria-hidden="true"></span>
      <p class="brand-name">Velt Harbor<br>Solutions</p>
    </div>

    <svg class="front-bands" viewBox="0 0 760 40" aria-hidden="true">
      <polygon points="0,22 480,22 480,40 0,40" fill="var(--brand-red)"/>
      <polygon points="494,6 760,6 760,40 494,40" fill="var(--navy)"/>
    </svg>
  </section>

  <section class="card card-back" aria-label="Business card back">
    <div class="brand-lockup" style="position:static;">
      <span class="brand-square" aria-hidden="true"></span>
      <p class="brand-name brand-name-back">Velt Harbor<br>Solutions</p>
    </div>
  </section>
</main>
</body>
</html>
```